Tarvimoor business cards

Need fresh design for our business cards. Logo must be specific, we are open for everything else.

Contact Information for Business Card

phrase "GMP & JANITORIAL SERVICES" should be used as main point of card

Colors
3176b5
3276b5
85acd3
cedeed
ffffff
0292cd
33a6d7
85cae6
cee9f5

Requirements
Must have
• The logo
Should not have
• crowded designs

```html
<!DOCTYPE html>
<html lang="en">
<head>
<meta charset="utf-8">
<title>Tarvimoor business cards</title>
<link rel="stylesheet" href="https://fonts.googleapis.com/css2?family=PT+Sans:wght@400;700&display=swap">
<style>
  :root {
    --brand-blue: #0f7cc4;
    --brand-blue-dark: #3176b5;
    --paper: #ffffff;
    --backdrop: #3b3e42;
    --ink-light: #ffffff;
  }
  * { margin: 0; padding: 0; box-sizing: border-box; }
  html, body {
    width: 1200px; height: 2164px; overflow: hidden;
    background: var(--backdrop);
    font-family: "PT Sans", Arial, sans-serif;
  }
  .canvas { position: relative; width: 1200px; height: 2164px; }
  .card {
    position: absolute; left: 100px; width: 1000px; height: 570px;
    border-radius: 26px; overflow: hidden; background: var(--paper);
    box-shadow: 0 18px 40px rgba(0,0,0,0.35);
  }
  .card-front { top: 430px; }
  .card-back { top: 1164px; }
  .card-shape { position: absolute; inset: 0; width: 100%; height: 100%; }

  .wordmark {
    position: absolute; color: var(--brand-blue);
    font-weight: 400; letter-spacing: 6px; text-transform: uppercase;
  }
  .card-front .wordmark { left: 40px; top: 254px; width: 430px; text-align: center; font-size: 50px; }

  .contact { position: absolute; left: 590px; top: 184px; color: var(--ink-light); }
  .contact-name { font-size: 44px; font-weight: 700; margin-bottom: 26px; }
  .contact-list { list-style: none; }
  .contact-item { display: flex; align-items: center; font-size: 30px; margin-bottom: 14px; }
  .contact-icon { width: 32px; height: 32px; margin-right: 18px; flex: none; }

  .card-back .wordmark { left: 420px; top: 248px; width: 470px; text-align: center; font-size: 64px; }
  .service-band {
    position: absolute; left: 420px; top: 340px; width: 470px; height: 58px;
    background: var(--brand-blue-dark); color: var(--ink-light);
    font-size: 32px; font-weight: 400; text-align: center; line-height: 58px;
    letter-spacing: 1px;
  }
</style>
</head>
<body>
<main class="canvas">

  <section class="card card-front" aria-label="Business card front">
    <svg class="card-shape" viewBox="0 0 1000 570" aria-hidden="true">
      <rect width="1000" height="570" fill="var(--brand-blue)"/>
      <circle cx="86" cy="285" r="424" fill="var(--paper)"/>
    </svg>
    <div class="wordmark">Tarvimoor</div>
    <div class="contact">
      <p class="contact-name">Your Namehere</p>
      <ul class="contact-list">
        <li class="contact-item">
          <svg class="contact-icon" viewBox="0 0 32 32" aria-hidden="true">
            <circle cx="16" cy="16" r="16" fill="#fff"/>
            <path d="M11 8.5l3 .5 1 4-2 1.5a10 10 0 0 0 4.5 4.5l1.5-2 4 1 .5 3c-1 1.5-3 2-4.5 1.5A14 14 0 0 1 9.5 13C9 11.5 9.5 9.5 11 8.5z" fill="var(--brand-blue)"/>
          </svg>
          1 (800) 555-0142
        </li>
        <li class="contact-item">
          <svg class="contact-icon" viewBox="0 0 32 32" aria-hidden="true">
            <circle cx="16" cy="16" r="16" fill="#fff"/>
            <rect x="11" y="8" width="10" height="5" fill="var(--brand-blue)"/>
            <rect x="8" y="13" width="16" height="8" rx="1.5" fill="var(--brand-blue)"/>
            <rect x="11" y="19" width="10" height="5" fill="var(--brand-blue)" stroke="#fff" stroke-width="1"/>
          </svg>
          (905) 555-0178
        </li>
        <li class="contact-item">
          <svg class="contact-icon" viewBox="0 0 32 32" aria-hidden="true">
            <circle cx="16" cy="16" r="16" fill="#fff"/>
            <rect x="8" y="10.5" width="16" height="11" rx="1.5" fill="var(--brand-blue)"/>
            <path d="M8.5 11.5l7.5 6 7.5-6" fill="none" stroke="#fff" stroke-width="1.5"/>
          </svg>
          info@tarvimoor.ca
        </li>
      </ul>
    </div>
  </section>

  <section class="card card-back" aria-label="Business card back">
    <svg class="card-shape" viewBox="0 0 1000 570" aria-hidden="true">
      <rect width="1000" height="570" fill="var(--paper)"/>
      <circle cx="-176" cy="285" r="456" fill="var(--brand-blue)"/>
    </svg>
    <div class="wordmark">Tarvimoor</div>
    <div class="service-band">GMP &amp; JANITORIAL SERVICES</div>
  </section>

</main>
</body>
</html>
```